Global Expert Network Firm needs business card design

We need business card design for a new company based in Seoul, South Korea called 'Corwell Insight Partners'. We recruit industry experts covering all countries and connect our client and recruited expert by phone, face-to-face meetings and etc. We are a global expert network firm that is focused on delivering high-quality experts to our clients throughout the world. Our clients include multinational corporations, global consulting firms, private equity firms, venture capital firms, asset management companies.
We have made new logo and please find attachment.(Please use new logo)
Target Market(s)
Global Consulting Firms, Investment Firms, Private Equity Firms, Venture Capital Firms.
Industry/Entity Type
Recruitment
Contact Information for Business Card
We need two Languages (English and Korean Version).
The front is Korean and the back is English version.
[The back] [English]
Company Name: Corwell Insight Partners, Inc.
CEO Name: Daniel Park
Address: #507, Hanbit Bldg, 82 Maebongsan-ro, Dobong-gu, Seoul, 01327, Korea
Tel. +82 2 718 4052
Fax. +82 2 864 1097
Mobile. +82 10 7264 8815
Email: daniel@corwellip.com
Web: www.corwellip.com
[The front] [Korean] => Described in same order as English version.
회사명: 코웰인사이트파트너스(주)
대표이사: 박도현
주소: 서울시 도봉구 매봉산로 82 한빛빌딩 507호
Tel. 02 718 4052
Fax. 02 864 1097
Mobile. 010 7264 8815
Web: www.corwellip.com
Look and feel
Each slider illustrates characteristics of the customer's brand and the style your logo design should communicate.

```html
<!DOCTYPE html>
<html lang="en">
<head>
<meta charset="utf-8">
<title>Corwell Insight Partners — Business Cards</title>
<link rel="stylesheet" href="https://fonts.googleapis.com/css2?family=Arimo:wght@400;700&family=Noto+Sans+KR:wght@700;900&display=swap">
<style>
  :root {
    --page-bg: #e8e5df;
    --card-navy: #1c2558;
    --ink-white: #ffffff;
    --font-latin: "Arimo", Arial, sans-serif;
    --font-korean: "Noto Sans KR", "Arimo", sans-serif;
  }
  * { margin: 0; padding: 0; box-sizing: border-box; }
  html, body {
    width: 960px; height: 1200px; overflow: hidden;
    background: var(--page-bg);
  }
  .canvas { position: relative; width: 960px; height: 1200px; }
  .card {
    position: absolute; left: 164px; width: 632px; height: 371px;
    background: var(--card-navy); color: var(--ink-white);
    font-family: var(--font-latin);
  }
  .card--english { top: 203px; }
  .card--korean { top: 626px; font-family: var(--font-korean); }

  .brand-name {
    position: absolute; display: flex; align-items: center; gap: 9px;
    font-family: var(--font-latin); font-weight: 400; color: var(--ink-white);
    white-space: nowrap;
  }
  .brand-name__square {
    display: block; background: var(--ink-white); flex: none;
  }
  .card--english .brand-name { left: 27px; top: 192px; font-size: 20px; }
  .card--english .brand-name__square { width: 14px; height: 14px; }
  .card--korean .brand-name { right: 34px; top: 82px; font-size: 15px; gap: 7px; }
  .card--korean .brand-name__square { width: 11px; height: 11px; }

  .card--english .holder-name {
    position: absolute; right: 28px; top: 95px;
    font-size: 27px; font-weight: 700;
  }
  .card--english .contact-block {
    position: absolute; right: 28px; top: 161px; text-align: right;
    font-size: 19px; line-height: 21.8px; font-style: normal;
  }
  .contact-block .company-name { font-weight: 700; }
  .card--english .email { position: absolute; right: 28px; top: 337px; font-size: 18.5px; }
  .card--english .website { position: absolute; left: 27px; top: 337px; font-size: 19px; }

  .card--korean .holder-name {
    position: absolute; left: 25px; top: 48px;
    font-size: 38px; font-weight: 900; line-height: 1.2;
  }
  .card--korean .company-name {
    position: absolute; left: 25px; top: 175px; font-size: 18px; font-weight: 700;
  }
  .card--korean .contact-block {
    position: absolute; left: 25px; top: 222px; font-size: 17px; font-weight: 700;
    line-height: 21.5px; font-style: normal;
  }
  .card--korean .contact-block .latin { font-family: var(--font-latin); }
  .card--korean .website {
    position: absolute; right: 34px; top: 310px;
    font-family: var(--font-latin); font-size: 19.5px; font-weight: 400;
  }
</style>
</head>
<body>
<main class="canvas">
  <section class="card card--english" aria-label="English side">
    <div class="brand-name"><span class="brand-name__square"></span>Corwell Insight Partners</div>
    <h1 class="holder-name">Daniel Park</h1>
    <address class="contact-block">
      <div class="company-name">Corwell Insight Partners, Inc.</div>
      <div>#507, Hanbit Bldg,</div>
      <div>82 Maebongsan-ro,</div>
      <div>Dobong-gu, Seoul, 01327, Korea</div>
      <div>Tel. +82 2 718 4052</div>
      <div>Fax. +82 2 864 1097</div>
      <div>Mobile. +82 10 7264 8815</div>
    </address>
    <div class="website">www.corwellip.com</div>
    <div class="email">Email: daniel@corwellip.com</div>
  </section>

  <section class="card card--korean" lang="ko" aria-label="Korean side">
    <h1 class="holder-name">박도현</h1>
    <div class="brand-name" lang="en"><span class="brand-name__square"></span>Corwell Insight Partners</div>
    <div class="company-name">코웰인사이트파트너스(주)</div>
    <address class="contact-block">
      <div>서울시 도봉구 매봉산로 82 한빛빌딩 507호</div>
      <div class="latin">Tel. 02 718 4052</div>
      <div class="latin">Fax. 02 864 1097</div>
      <div class="latin">Mobile. 010 7264 8815</div>
      <div class="latin">Email: daniel@corwellip.com</div>
    </address>
    <div class="website">www.corwellip.com</div>
  </section>
</main>
</body>
</html>
```